Designing a Chocolate Bar's Package

We are a chocolate manufacturing company located in Lebanon. We produce chocolate on a wholesale level, and we are planning a new line of production at the moment.
We intend to be make small chocolate bars (about 30g) similar to the "Varmo Radiance" bar with several flavors. 2 flavors have been decided so far (Mint flavored dark chocolate and Plain dark chocolate).
The packaging material will be similar to varmo's package as well. It won't be a carton box. It'll be some sort of paper wrapping the entire bar. So I am looking for a design that has a unique and cool front and back look.
If only one design is to be prepared, please choose either the mint's flavor or the plain dark chocolate, and prepare the design accordingly.
Updates
Project Deadline Extended
Reason: I still have some time to begin the production. The new deadline,therefore, is the end of this month.
Target Market(s)
basically all chocolate lovers...
Industry/Entity Type
It Company
Requirements
Must have
- I will be uploading our logo. Please make sure to use it in the design.

```html
<!DOCTYPE html>
<html lang="en">
<head>
<meta charset="UTF-8">
<title>Corvella Dark Chocolate Wrappers</title>
<link rel="stylesheet" href="https://fonts.googleapis.com/css2?family=Open+Sans:wght@300;400&family=Pinyon+Script&display=swap">
<style>
  :root {
    --backdrop: #d4d5d6;
    --band-top: #2c0e09;
    --band-bottom: #1c0604;
    --gold-light: #f1dca0;
    --gold-mid: #c9a35a;
    --gold-dark: #8d6a2c;
    --mint-center: #6fd845;
    --mint-mid: #3fb52b;
    --mint-edge: #1b7a1c;
    --plain-center: #f8b125;
    --plain-mid: #e95a1e;
    --plain-edge: #c01a1a;
    --chocolate-light: #6e4a3c;
    --chocolate-dark: #3a2019;
    --leaf: #7cc65a;
    --ink-light: #ffffff;
  }
  * { box-sizing: border-box; margin: 0; padding: 0; }
  html, body {
    width: 1162px;
    height: 1200px;
    overflow: hidden;
    background: var(--backdrop);
  }
  .canvas {
    position: relative;
    width: 1162px;
    height: 1200px;
  }
  .wrapper {
    position: absolute;
    top: 100px;
    width: 447px;
    height: 1011px;
    border-radius: 12px;
    overflow: hidden;
    box-shadow: 0 3px 10px rgba(0,0,0,0.18);
  }
  .wrapper--mint { left: 118px; background: radial-gradient(ellipse 70% 55% at 50% 55%, var(--mint-center), var(--mint-mid) 55%, var(--mint-edge)); }
  .wrapper--plain { left: 597px; background: radial-gradient(ellipse 70% 55% at 50% 58%, var(--plain-center), var(--plain-mid) 50%, var(--plain-edge)); }

  .seal {
    position: absolute;
    left: 0; right: 0;
    height: 22px;
    background: linear-gradient(90deg, var(--gold-dark), var(--gold-light) 30%, var(--gold-mid) 60%, var(--gold-light) 85%, var(--gold-dark));
    z-index: 2;
  }
  .seal--top { top: 0; }
  .seal--bottom { bottom: 0; }

  .brand-band {
    position: absolute;
    top: 0; left: 0; right: 0;
    height: 302px;
    background: linear-gradient(180deg, var(--band-top), var(--band-bottom));
    border-bottom: 2px solid var(--gold-mid);
    text-align: center;
  }
  .brand-name {
    position: absolute;
    top: 100px;
    left: 0; right: 0;
    font-family: "Open Sans", sans-serif;
    font-weight: 300;
    font-size: 72px;
    letter-spacing: 1px;
    color: var(--ink-light);
  }
  .tagline {
    position: absolute;
    top: 224px;
    left: 0; right: 0;
    font-family: "Pinyon Script", cursive;
    font-size: 34px;
    color: var(--ink-light);
  }

  .product-shot {
    position: absolute;
    left: 94px;
    top: 409px;
    width: 262px;
    height: 295px;
    border-radius: 6px;
    background: linear-gradient(135deg, var(--chocolate-dark) 0%, var(--chocolate-light) 50%, var(--chocolate-dark) 100%);
  }
  .product-shot--mint {
    background:
      radial-gradient(ellipse 38% 30% at 62% 82%, var(--leaf) 0%, var(--leaf) 60%, transparent 62%),
      linear-gradient(135deg, var(--chocolate-dark) 0%, var(--chocolate-light) 50%, var(--chocolate-dark) 100%);
  }

  .flavor {
    position: absolute;
    left: 0; right: 0;
    text-align: center;
    color: var(--ink-light);
    font-family: "Open Sans", sans-serif;
  }
  .flavor__note { top: 896px; font-size: 29px; font-weight: 300; }
  .flavor__name { top: 936px; font-size: 40px; font-weight: 400; }
  .flavor__weight { top: 1010px; font-size: 31px; font-weight: 400; }
  .wrapper .flavor__note { top: 793px; }
  .wrapper .flavor__name { top: 835px; }
  .wrapper .flavor__weight { top: 905px; }
</style>
</head>
<body>
<main class="canvas">

  <section class="wrapper wrapper--mint" aria-label="Mint flavored dark chocolate wrapper">
    <div class="seal seal--top"></div>
    <header class="brand-band">
      <div class="brand-name">Corvella</div>
      <div class="tagline">Quality Chocolate</div>
    </header>
    <div class="product-shot product-shot--mint" role="img" aria-label="Photo of a dark chocolate square with fresh mint leaves"></div>
    <p class="flavor flavor__note">mint flavored</p>
    <p class="flavor flavor__name">Dark Chocolate</p>
    <p class="flavor flavor__weight">30g</p>
    <div class="seal seal--bottom"></div>
  </section>

  <section class="wrapper wrapper--plain" aria-label="Plain dark chocolate wrapper">
    <div class="seal seal--top"></div>
    <header class="brand-band">
      <div class="brand-name">Corvella</div>
      <div class="tagline">Quality Chocolate</div>
    </header>
    <div class="product-shot" role="img" aria-label="Photo of a dark chocolate square"></div>
    <p class="flavor flavor__note">plain</p>
    <p class="flavor flavor__name">Dark Chocolate</p>
    <p class="flavor flavor__weight">30g</p>
    <div class="seal seal--bottom"></div>
  </section>

</main>
</body>
</html>
```